Hosvin Logo and business card

We need a business card and logo, we are currently using a logo that we like but would like to be a bit more streamlined. We deal with very high end clients and our business card needs to reflect that. We would love to see and hire somebody that can deliver a very MODERN, simple design. With he main front of the card to be black with either a red lettering or White to provide great contrast. I would like to have a minimalist abstract picture of a heavy machine on it but it is not a requirement ( most likely an Crane ( a brisk otter crane with a bucket would be perfect or maybe a vendrel 820 TX )) If it keeps in line with being a classic simple, and modern design. Letterpress is also an option where it gives it a great look and texture, the card will be printed on a thick stock. On the back there needs to be a star included somewhere on the card and design, this represents the first generation that started the company back in 1936 therefore it is a sentimental addition ( make it modern and simple)
We do not want a cheesy construction template. We do heavy site work, aka we use excavators, payloaders, off road jox m41 trucks, very big fun toys.
There is a huge chance to get the web design as well for the winning design.
Have fun, cannot wait to see the designs!
In addition, we'd like to point out that our primary need and priority is still the BUSINESS CARD design itself. The logo has to complement the overall look of the business card, but it is secondary to the card's look. Please keep this in mind.
Thank you,
Gideon
Target Market(s)
General Contractors, upscale home owners ( house values of 1M plus)
and commercial property owners.
Projects range from $5000 to 1 million.
Industry/Entity Type
Construction
Requirements
Must have
- Star incorporated into design
Nice to have
- an abstract heavy site work machine ( pics attached) If it keeps in line with being a classic simple, and modern design.
I would like to have black and red on the design since all the lettering on the trucks is red, but i will let the designer take care of that.

```html
<!DOCTYPE html>
<html lang="en">
<head>
<meta charset="utf-8">
<title>Hosvin Industries – Business Card</title>
<link href="https://fonts.googleapis.com/css2?family=Michroma&family=Overpass:wght@400;600&display=swap" rel="stylesheet">
<style>
  :root {
    --brand-red: #e8202a;
    --card-black: #000000;
    --ink-white: #ffffff;
    --ink-grey: #a8a8a8;
    --frame-white: #ffffff;
    --stage-dark: #050505;
    --stage-light: #c9c9c9;
  }
  * { margin: 0; padding: 0; box-sizing: border-box; }
  html, body { width: 1000px; height: 1200px; overflow: hidden; }
  body {
    position: relative;
    background: radial-gradient(ellipse 80% 70% at 50% 100%, var(--stage-light) 0%, #8a8a8a 45%, #2a2a2a 80%, var(--stage-dark) 100%);
    font-family: "Overpass", Arial, sans-serif;
  }
  .brand-title {
    position: absolute;
    top: 104px; left: 0; width: 1000px;
    text-align: center;
    font-family: "Michroma", Arial, sans-serif;
    font-size: 78px;
    line-height: 100px;
    color: var(--brand-red);
    letter-spacing: 2px;
  }
  .card {
    position: absolute;
    left: 120px; width: 758px;
    background: var(--card-black);
    border: 2px solid var(--frame-white);
    box-shadow: 0 10px 22px rgba(0,0,0,0.45);
  }
  .card--front { top: 267px; height: 421px; }
  .card--back { top: 723px; height: 423px; }

  .machine-art {
    position: absolute;
    left: 150px; top: 70px;
    width: 420px; height: 270px;
    background:
      radial-gradient(circle at 95px 135px, rgba(232,32,42,0.85) 0%, rgba(232,32,42,0.35) 40px, rgba(232,32,42,0) 95px),
      radial-gradient(ellipse at 65% 50%, rgba(120,14,20,0.35) 0%, rgba(0,0,0,0) 70%);
  }
  .front-wordmark {
    position: absolute;
    left: 0; top: 188px; width: 100%;
    text-align: center;
    font-family: "Michroma", Arial, sans-serif;
    font-size: 29px;
    color: var(--ink-white);
    letter-spacing: 0.5px;
  }

  .contact {
    position: absolute;
    top: 98px; left: 0; width: 100%;
    text-align: center;
    font-size: 19px;
    line-height: 24px;
    color: var(--ink-grey);
  }
  .contact__name { color: var(--ink-white); font-weight: 600; letter-spacing: 0.5px; }
  .heritage-mark {
    position: absolute;
    left: 348px; top: 244px;
  }
  .heritage-year {
    position: absolute;
    top: 318px; left: 0; width: 100%;
    text-align: center;
    font-family: Arial, Helvetica, sans-serif;
    font-weight: 700;
    font-size: 13px;
    color: var(--brand-red);
  }
  .back-rule {
    position: absolute;
    top: 345px; left: 204px;
    width: 350px; height: 2px;
    background: var(--brand-red);
  }
  .back-wordmark {
    position: absolute;
    top: 360px; left: 0; width: 100%;
    text-align: center;
    font-family: "Michroma", Arial, sans-serif;
    font-size: 17px;
    color: var(--ink-white);
  }
</style>
</head>
<body>
  <div class="brand-title">HOSVIN</div>

  <section class="card card--front">
    <div class="machine-art" role="img" aria-label="Red line drawing of an excavator bucket with teeth, lit by a red glow"></div>
    <div class="front-wordmark">HOSVIN INDUSTRIES INC</div>
  </section>

  <section class="card card--back">
    <div class="contact">
      <div class="contact__name">GIDEON HOSVIN</div>
      <div>PROJECT MANAGER</div>
      <div>+315 604 7183</div>
      <div>gideon@hosvin.com</div>
      <div>Plot 9K, Northgate, Lindmoor, 0417</div>
    </div>
    <svg class="heritage-mark" width="60" height="60" viewBox="0 0 60 60" aria-hidden="true">
      <circle cx="30" cy="30" r="28" fill="var(--brand-red)"/>
    </svg>
    <div class="heritage-year">Since 1936</div>
    <div class="back-rule"></div>
    <div class="back-wordmark">HOSVIN INDUSTRIES INC</div>
  </section>
</body>
</html>
```